" Marca de móveis planejados destinada exclusivamente a clientes proprietario de apartamentos novos de construtoras e imobiliárias parceiras. Trata-se de móveis com preços acessíveis, elegantes e de boa qualidade. "

```html
<!DOCTYPE html>
<html lang="pt-BR">
<head>
<meta charset="utf-8">
<title>Serena Móveis — Cartão de visita</title>
<link href="https://fonts.googleapis.com/css2?family=Open+Sans:wght@400;600&display=swap" rel="stylesheet">
<style>
  :root {
    --navy: #0d2a52;
    --white: #ffffff;
    --ink: #1f2a3a;
    --muted: #9a9fa6;
    --backdrop: #e9eaec;
  }
  * { margin: 0; padding: 0; box-sizing: border-box; }
  html, body { width: 1200px; height: 1200px; overflow: hidden; }
  body {
    background: var(--backdrop);
    font-family: "Open Sans", Arial, sans-serif;
    position: relative;
  }
  .business-card {
    position: absolute;
    left: 100px; top: 392px;
    width: 1000px; height: 415px;
    background: var(--white);
    overflow: hidden;
  }
  .contact-panel {
    position: absolute;
    left: 537px; top: 0;
    width: 463px; height: 100%;
    background: var(--navy);
  }
  .icon-tab {
    position: absolute;
    left: 520px; top: 75px;
    width: 34px; height: 270px;
    background: var(--white);
    border-radius: 0 16px 16px 0;
  }
  .brand-name {
    position: absolute;
    left: 61px; top: 52px;
    width: 366px;
    text-align: center;
    color: var(--navy);
    font-weight: 600;
    text-transform: uppercase;
    line-height: 1;
  }
  .brand-name .primary { display: block; font-size: 58px; letter-spacing: 6px; }
  .brand-name .secondary { display: block; font-size: 20px; letter-spacing: 14px; margin-top: 12px; }
  .person {
    position: absolute;
    left: 61px; top: 190px;
    padding-left: 20px;
    border-left: 9px solid var(--navy);
    height: 68px;
  }
  .person-name { font-size: 26px; color: var(--ink); line-height: 1.2; }
  .person-role { font-size: 17px; color: var(--ink); text-align: right; letter-spacing: 1px; }
  .social {
    position: absolute;
    top: 362px;
    display: flex; align-items: center; gap: 8px;
    font-size: 13px; color: var(--muted);
  }
  .social .dot {
    width: 34px; height: 34px; border-radius: 50%;
    background: #c9ccd0;
  }
  .social-a { left: 232px; }
  .social-b { left: 398px; }
  .contact-row {
    position: absolute;
    left: 578px;
    color: var(--white);
    font-size: 21px;
    line-height: 1.2;
  }
  .contact-icon {
    position: absolute;
    left: 521px;
    width: 32px; height: 32px;
  }
</style>
</head>
<body>
  <div class="business-card">
    <div class="contact-panel"></div>
    <div class="icon-tab"></div>

    <div class="brand-name">
      <span class="primary">Serena</span>
      <span class="secondary">Móveis</span>
    </div>

    <div class="person">
      <div class="person-name">Nome Sobrenome</div>
      <div class="person-role">cargo</div>
    </div>

    <div class="social social-a"><span class="dot"></span>/serenamoveis</div>
    <div class="social social-b"><span class="dot"></span>@serenamoveis</div>

    <svg class="contact-icon" style="top:96px" viewBox="0 0 32 32" aria-hidden="true">
      <circle cx="16" cy="16" r="15" fill="var(--white)"/>
      <path d="M16 7a6 6 0 0 0-6 6c0 4.5 6 12 6 12s6-7.5 6-12a6 6 0 0 0-6-6zm0 8.5a2.5 2.5 0 1 1 0-5 2.5 2.5 0 0 1 0 5z" fill="var(--navy)"/>
    </svg>
    <div class="contact-row" style="top:92px">Endereço Completo<br>Bairro - Cidade - Estado - Cep</div>

    <svg class="contact-icon" style="top:162px" viewBox="0 0 32 32" aria-hidden="true">
      <circle cx="16" cy="16" r="15" fill="var(--white)"/>
      <g fill="none" stroke="var(--navy)" stroke-width="1.8">
        <circle cx="16" cy="16" r="8"/>
        <ellipse cx="16" cy="16" rx="3.5" ry="8"/>
        <path d="M8 16h16M9.5 12h13M9.5 20h13"/>
      </g>
    </svg>
    <div class="contact-row" style="top:165px">www.serenamoveis.com.br</div>

    <svg class="contact-icon" style="top:222px" viewBox="0 0 32 32" aria-hidden="true">
      <circle cx="16" cy="16" r="15" fill="var(--white)"/>
      <rect x="8.5" y="10.5" width="15" height="11" rx="1.5" fill="var(--navy)"/>
      <path d="M9 11.5l7 5.5 7-5.5" fill="none" stroke="var(--white)" stroke-width="1.4"/>
    </svg>
    <div class="contact-row" style="top:225px">contato@serenamoveis.com.br</div>

    <svg class="contact-icon" style="top:284px" viewBox="0 0 32 32" aria-hidden="true">
      <circle cx="16" cy="16" r="15" fill="var(--white)"/>
      <path d="M11.5 8.5l3 3.2-1.8 2.3c1 2.2 2.8 4 5 5l2.3-1.8 3.2 3-1.7 2.6c-6.8-.6-12-5.8-12.6-12.6z" fill="var(--navy)"/>
    </svg>
    <div class="contact-row" style="top:272px">11 90000-1234<br>11 90000-5678</div>
  </div>
</body>
</html>
```